Vital Spark Electrical in need of a business card design

We need a new business card designed for our electrical business. We have a logo already which I will attach below.
Would like the business card to be..
-BLACK background preferably, possibly white back ground behind logo if colours clash.
-White & Blue (logo blue) text
Something that makes the logo pop, & a modern look. Possibly minimal clean format.

REQUIRE:
-Logo on front & back

TEXT TO INCLUDE (ON ONE SIDE):

Tom Harlow
Director/Electrician
M: 0417 365 208
E:info@vitalsparkelectrical-example.com.au
W:www.vitalsparkelectrical-example.com.au
R.E.C 57318

Custom/New Homes
Renovations
Commercial Office/Shop Fit-outs
Communications & Security Cameras
Electric Vehicle Chargers
Airconditioning
Updates

Requirements
Nice to have
• Possibly even lighten the grey shades for the words 'Vital' & 'Spark' to be more easily read on a black background.

```html
<!DOCTYPE html>
<html lang="en">
<head>
<meta charset="utf-8">
<title>Vital Spark Electrical – Business Card</title>
<link href="https://fonts.googleapis.com/css2?family=Open+Sans:wght@400;600&display=swap" rel="stylesheet">
<style>
  :root {
    --bg: #0c0c0d;
    --card: #1a1a1b;
    --blue: #0aa3e0;
    --white: #f1f1f1;
    --grey: #c9c9c9;
    --rule: #6a6a6a;
  }
  * { box-sizing: border-box; margin: 0; padding: 0; }
  html, body {
    width: 1200px; height: 900px; overflow: hidden;
    background: var(--bg);
    font-family: "Open Sans", sans-serif;
  }
  .stage {
    position: relative; width: 1200px; height: 900px;
    display: flex; flex-direction: column; align-items: center; justify-content: center; gap: 44px;
  }
  .card {
    position: relative; width: 600px; height: 343px;
    background: var(--card);
    box-shadow: 0 10px 30px rgba(0,0,0,.6);
    overflow: hidden;
  }
  .card__band {
    position: absolute; left: 0; right: 0; bottom: 0; height: 9px; background: var(--blue);
  }

  /* Front */
  .front { display: flex; flex-direction: column; align-items: center; padding-top: 92px; }
  .brand { display: flex; align-items: center; gap: 16px; }
  .brand__mark { width: 34px; height: 34px; background: var(--blue); }
  .brand__name { font-size: 34px; font-weight: 600; color: var(--white); letter-spacing: .5px; }
  .services {
    margin-top: 52px; text-align: center; color: var(--white);
    font-size: 14.5px; line-height: 1.45; letter-spacing: .3px;
  }
  .services__dot {
    display: inline-block; width: 7px; height: 7px; border-radius: 50%;
    background: var(--blue); margin: 0 7px; vertical-align: 2px;
  }

  /* Back */
  .back { display: flex; flex-direction: column; align-items: center; padding-top: 60px; }
  .contact__name { font-size: 31px; font-weight: 600; color: var(--blue); line-height: 1.1; }
  .contact__role { font-size: 15px; color: var(--grey); margin-top: 2px; letter-spacing: .3px; }
  .icon-row { display: flex; align-items: center; gap: 8px; margin-top: 10px; }
  .icon-row__rule { width: 86px; height: 1px; background: var(--rule); }
  .icon { width: 26px; height: 26px; border-radius: 4px; background: var(--blue); display: flex; align-items: center; justify-content: center; }
  .icon svg { width: 16px; height: 16px; }
  .contact__lines {
    margin-top: 8px; text-align: center; color: var(--white);
    font-size: 14.5px; line-height: 1.5; letter-spacing: .3px;
  }
  .contact__rule { width: 320px; height: 1px; background: var(--rule); margin-top: 12px; }
  .licence { margin-top: 14px; font-size: 15px; color: var(--white); letter-spacing: .3px; }
  .licence__label { color: var(--blue); }
</style>
</head>
<body>
<main class="stage">
  <section class="card front" aria-label="Card front">
    <div class="brand">
      <span class="brand__mark"></span>
      <span class="brand__name">Vital Spark Electrical</span>
    </div>
    <p class="services">
      Custom/New Homes<span class="services__dot"></span>Renovations<span class="services__dot"></span>Airconditioning<br>
      Communications &amp; Security Cameras<span class="services__dot"></span>Electric Vehicle Chargers<br>
      Commercial Office/Shop Fit-outs
    </p>
    <div class="card__band"></div>
  </section>

  <section class="card back" aria-label="Card back">
    <h1 class="contact__name">Tom Harlow</h1>
    <p class="contact__role">Director/Electrician</p>
    <div class="icon-row">
      <span class="icon-row__rule"></span>
      <span class="icon" aria-label="Phone">
        <svg viewBox="0 0 16 16"><path d="M2 5c0-2 2-3 6-3s6 1 6 3l-3 1-1-2H6L5 6 2 5zM4 8h8l1 5H3z" fill="#1a1a1b"/></svg>
      </span>
      <span class="icon" aria-label="Email">
        <svg viewBox="0 0 16 16"><rect x="1.5" y="3.5" width="13" height="9" fill="none" stroke="#1a1a1b" stroke-width="1.5"/><path d="M1.5 3.5 8 9l6.5-5.5M1.5 12.5 6 7.5M14.5 12.5 10 7.5" fill="none" stroke="#1a1a1b" stroke-width="1.2"/></svg>
      </span>
      <span class="icon" aria-label="Website">
        <svg viewBox="0 0 16 16"><circle cx="8" cy="8" r="6.5" fill="none" stroke="#1a1a1b" stroke-width="1.5"/><ellipse cx="8" cy="8" rx="2.8" ry="6.5" fill="none" stroke="#1a1a1b" stroke-width="1.2"/><path d="M1.5 8h13" stroke="#1a1a1b" stroke-width="1.2"/></svg>
      </span>
      <span class="icon-row__rule"></span>
    </div>
    <p class="contact__lines">
      0417 365 208<br>
      info@vitalsparkelectrical-example.com.au<br>
      www.vitalsparkelectrical-example.com.au
    </p>
    <div class="contact__rule"></div>
    <p class="licence"><span class="licence__label">R.E.C</span> 57318</p>
    <div class="card__band"></div>
  </section>
</main>
</body>
</html>
```